(Grindstone Nook) sourcing coffee related material and services

we are a start up that provide all coffee related items for coffee shops and coffee fanatics. However, we mostly offer coffee machines customization that includes paint replacement and wood modification. we also focus on providing training for barista and coffee lovers.

we are looking for the following:

1-Design a logo that will be used for social media application and official paper work requirements

2- Design a business card (square shaped 2"*2") adopting the same logo and identity. please allow for adding mobile number, blinkpost, and instgram accounts in the card.

3- Design a very basic monogram stamp by adding the three character (R4T) the number (2) shall be small in size just like how the numbers written in chemical formal.

Please take a quick look to crumbleframe page to have a idea about the our start up

https://www.crumbleframe.example/grindstone_nook/

Target Market(s)

coffeeshop owners and coffee fanatics

Industry/Entity Type

Coffee Shop

Contact Information for Business Card

R4T
Grindstone Nook
editable text to add links to socail media

Logo Text

R4T

Font styles to use
Other font styles liked:
• flat design fonts

Colors

Designer to choose colors to be used in the design.

Requirements
Must have
• espresso portafilter, simple and minimal industrial look, wood,
Nice to have
• wood-making, portafilter, coffee beans, coffee tree,

```html
<!DOCTYPE html>
<html lang="en">
<head>
<meta charset="utf-8">
<title>Grindstone Nook – Business Card</title>
<link rel="stylesheet" href="https://fonts.googleapis.com/css2?family=Fira+Sans:wght@700&family=Jost:wght@300&display=swap">
<style>
  :root {
    --page-bg: #ffffff;
    --card-bg: #ffffff;
    --card-border: #2b2b2b;
    --brand-orange: #e8951f;
    --label-grey: #9b9078;
    --steel-light: #d9dad7;
    --steel-mid: #9a9c99;
    --steel-dark: #3e3f3e;
    --bean-light: #8a5535;
    --bean-mid: #5a341f;
    --bean-dark: #2c170c;
    --white: #ffffff;
  }
  * { margin: 0; padding: 0; box-sizing: border-box; }
  html, body {
    width: 1200px;
    height: 1000px;
    overflow: hidden;
    background: var(--page-bg);
  }
  .canvas {
    position: relative;
    width: 1200px;
    height: 1000px;
  }
  .card {
    position: absolute;
    left: 326px;
    top: 226px;
    width: 548px;
    height: 548px;
    border: 1px solid var(--card-border);
    background: var(--card-bg);
    overflow: hidden;
  }
  .info-panel {
    position: absolute;
    left: 0;
    top: 0;
    width: 340px;
    height: 546px;
  }
  .wordmark {
    position: absolute;
    left: 64px;
    top: 62px;
    font-family: "Fira Sans", sans-serif;
    font-weight: 700;
    font-size: 112px;
    line-height: 1;
    letter-spacing: 2px;
    color: var(--brand-orange);
  }
  .business-name {
    position: absolute;
    left: 65px;
    top: 220px;
    font-family: "Fira Sans", sans-serif;
    font-weight: 700;
    font-size: 25px;
    line-height: 1;
    letter-spacing: 0.3px;
    color: var(--brand-orange);
  }
  .contact-list {
    position: absolute;
    left: 60px;
    top: 284px;
    list-style: none;
  }
  .contact-item {
    display: flex;
    align-items: center;
    height: 40px;
    margin-bottom: 22.5px;
  }
  .contact-icon {
    width: 40px;
    height: 40px;
    flex: none;
  }
  .contact-label {
    margin-left: 19px;
    margin-top: -10px;
    font-family: "Jost", sans-serif;
    font-weight: 300;
    font-size: 15px;
    letter-spacing: 0.6px;
    color: var(--label-grey);
  }
  .photo-machine {
    position: absolute;
    left: 340px;
    top: 0;
    width: 208px;
    height: 275px;
    background: linear-gradient(160deg, var(--steel-light) 0%, var(--steel-mid) 55%, var(--steel-dark) 100%);
  }
  .photo-beans {
    position: absolute;
    left: 340px;
    top: 275px;
    width: 208px;
    height: 273px;
    background: radial-gradient(circle at 40% 40%, var(--bean-light) 0%, var(--bean-mid) 55%, var(--bean-dark) 100%);
  }
  .beans-wordmark {
    position: absolute;
    left: 52px;
    top: 96px;
    font-family: "Fira Sans", sans-serif;
    font-weight: 700;
    font-size: 60px;
    line-height: 1;
    color: var(--white);
  }
  .beans-name {
    position: absolute;
    left: 52px;
    top: 182px;
    font-family: "Fira Sans", sans-serif;
    font-weight: 700;
    font-size: 13px;
    line-height: 1;
    color: var(--white);
  }
</style>
</head>
<body>
<div class="canvas">
  <div class="card">
    <section class="info-panel">
      <div class="wordmark">R4T</div>
      <div class="business-name">Grindstone Nook</div>
      <ul class="contact-list">
        <li class="contact-item">
          <svg class="contact-icon" viewBox="0 0 40 40"><circle cx="20" cy="20" r="19" fill="none" stroke="var(--brand-orange)" stroke-width="2"/><circle cx="20" cy="20" r="16" fill="var(--brand-orange)"/></svg>
          <span class="contact-label">brewfeed</span>
        </li>
        <li class="contact-item">
          <svg class="contact-icon" viewBox="0 0 40 40"><circle cx="20" cy="20" r="19" fill="none" stroke="var(--brand-orange)" stroke-width="2"/><circle cx="20" cy="20" r="16" fill="var(--brand-orange)"/></svg>
          <span class="contact-label">crumbleframe</span>
        </li>
        <li class="contact-item">
          <svg class="contact-icon" viewBox="0 0 40 40"><circle cx="20" cy="20" r="19" fill="none" stroke="var(--brand-orange)" stroke-width="2"/><circle cx="20" cy="20" r="16" fill="var(--brand-orange)"/></svg>
          <span class="contact-label">blinkpost</span>
        </li>
        <li class="contact-item">
          <svg class="contact-icon" viewBox="0 0 40 40"><circle cx="20" cy="20" r="19" fill="none" stroke="var(--brand-orange)" stroke-width="2"/><circle cx="20" cy="20" r="16" fill="var(--brand-orange)"/><rect x="15" y="11" width="10" height="18" rx="2" fill="var(--white)"/><rect x="16.5" y="13" width="7" height="13" fill="var(--brand-orange)"/></svg>
          <span class="contact-label">phone</span>
        </li>
      </ul>
    </section>
    <div class="photo-machine" role="img" aria-label="Chrome lever espresso machine pouring into a white cup"></div>
    <div class="photo-beans" role="img" aria-label="Roasted coffee beans background">
      <div class="beans-wordmark">R4T</div>
      <div class="beans-name">Grindstone Nook</div>
    </div>
  </div>
</div>
</body>
</html>
```